We need business cards for our Kashmiri Indian Takeaway Shop. our business sells authentic Kashmiri Cuisine. We also offer catering services and have a BYO Function Room available for private bookings. We would like to see simple but stylish designs that feature Moroccan or Arabic style patterns/ borders and use golds, deep reds, pearl/cream and a touch of black or white. We do not want pictures of curries or Indian spices, chillies etc. The final design should communicate sumptuous, exotic dining.

Target Market(s)

Indian food lovers

Industry/Entity Type

Catering

Contact Information for Business Card

Rafi's Kitchen Authentic Kashmiri Indian Cuisine

Colors
ec2027
fce8d3
fcca95
faa54b

Requirements
Must have
• Simple but stylish design, using Moroccan/Arabic inspired borders or features
Should not have
• Pictures of curries, spices, food etc

```html
<!DOCTYPE html>
<html lang="en">
<head>
<meta charset="utf-8">
<title>Rafi's Kitchen – Business Card</title>
<link rel="stylesheet" href="https://fonts.googleapis.com/css2?family=Open+Sans:wght@400;600;700;800&display=swap">
<style>
  :root {
    --backdrop: #2b2b2b;
    --card-white: #ffffff;
    --card-shade: #ececec;
    --brand-red: #e3202a;
    --spice-orange: #f5a04a;
    --ink-grey: #3a3a3a;
    --pattern-brown: #8a5a36;
    --pattern-cream: #e9d3b4;
  }
  * { margin: 0; padding: 0; box-sizing: border-box; }
  html, body {
    width: 1200px;
    height: 900px;
    overflow: hidden;
    background: var(--backdrop);
    font-family: "Open Sans", Arial, sans-serif;
  }
  .business-card {
    position: absolute;
    left: 100px;
    top: 164px;
    width: 1000px;
    height: 572px;
    background: linear-gradient(135deg, var(--card-shade) 0%, var(--card-white) 45%, var(--card-white) 100%);
    overflow: hidden;
  }
  .pattern-border {
    position: absolute;
    left: 0;
    width: 100%;
    height: 28px;
    background: linear-gradient(90deg, var(--pattern-brown), #a57247 50%, var(--pattern-brown));
  }
  .pattern-border--top { top: 0; }
  .pattern-border--bottom { bottom: 0; }

  .brand {
    position: absolute;
    left: 0;
    top: 112px;
    width: 100%;
    text-align: center;
  }
  .brand-name {
    font-size: 88px;
    font-weight: 800;
    color: var(--brand-red);
    letter-spacing: 2px;
    line-height: 1;
  }
  .brand-tagline {
    margin-top: 4px;
    padding-left: 120px;
    font-size: 30px;
    font-weight: 700;
    color: var(--spice-orange);
  }
  .rule {
    position: absolute;
    height: 1px;
    background: linear-gradient(90deg, rgba(227,32,42,0), var(--brand-red) 40%, rgba(227,32,42,0));
  }
  .rule--upper { left: 330px; top: 262px; width: 540px; }
  .rule--lower { left: 120px; top: 376px; width: 760px; }

  .owner {
    position: absolute;
    left: 0;
    top: 318px;
    width: 100%;
    text-align: center;
    font-size: 34px;
  }
  .owner-name { font-weight: 700; color: var(--brand-red); }
  .owner-role { font-weight: 400; color: var(--spice-orange); font-size: 28px; }

  .contact {
    position: absolute;
    left: 0;
    top: 394px;
    width: 100%;
    text-align: center;
  }
  .contact-phone {
    font-size: 24px;
    font-weight: 700;
    color: var(--brand-red);
  }
  .contact-phone .value { color: var(--ink-grey); font-weight: 400; }
  .contact-address {
    margin-top: 8px;
    font-size: 25px;
    font-weight: 600;
    color: var(--ink-grey);
    line-height: 1.35;
  }
</style>
</head>
<body>
  <main class="business-card">
    <div class="pattern-border pattern-border--top" role="img" aria-label="Moroccan-style lattice pattern border in brown and cream"></div>

    <header class="brand">
      <h1 class="brand-name">Rafi's Kitchen</h1>
      <p class="brand-tagline">Authentic Kashmiri Indian Cuisine</p>
    </header>

    <div class="rule rule--upper"></div>

    <p class="owner">
      <span class="owner-name">Samir Rafi -</span>
      <span class="owner-role">Owner &amp; Chef</span>
    </p>

    <div class="rule rule--lower"></div>

    <section class="contact">
      <p class="contact-phone">Phone : <span class="value">07-4055 0123</span></p>
      <p class="contact-address">Takeaway Shop &amp; Catering, BYO Function Room - Booking<br>essential, 9 Cedar Lane, Yungaburra Qld</p>
    </section>

    <div class="pattern-border pattern-border--bottom" role="img" aria-label="Moroccan-style lattice pattern border in brown and cream"></div>
  </main>
</body>
</html>
```